Exclusive beauty salon needs a price list or services booklet

I need a new very attractive flyer for my beauty salon, containing information on the different services and their prices.
In attachment you can find a pdf of the "old" one, but I'd love to have a beautifully designed new one!
I'd love to have a booklet in format 148 x 148 mm, or in US format, containing 12 or 16 pages, but if you can offer other nice looking designs they are welcome!
The services that need to come in the booklet with their prices can all be found on my website: www.atelierkova.be, starting with
Gelaatsverzorging
Wimperverlenging
Suikerontharing
Wimperlifting
Permanente Make Up
Airbrush Tanning

Target Market(s)

woman from 20 to 89 years old

Industry/Entity Type

Beauty Salon

Font styles to use
Sans Serif

Colors

Designer to choose colors to be used in the design.

Requirements
Must have
• a classy nice look, it must contain details about the services from my beauty salon and their prices, and nice pictures.
• The Names, prices and explanations of the services can easily be found on my website: www.atelierkova.be
Nice to have
• In attachment you can find the "old" price list in pdf, what I need now is a "new booklet" with the new logo and updated services price list.
• I need a very nice and attractive looking booklet, classy chique, Paris chique, looking very expensive.
Should not have
• Not too much colors, not too curly, but still feminine

```html
<!DOCTYPE html>
<html lang="nl">
<head>
<meta charset="utf-8">
<title>Atelier Kova – Behandelingen en tarieven</title>
<link rel="stylesheet" href="https://fonts.googleapis.com/css2?family=Open+Sans:ital,wght@0,300;0,400;0,600;1,300;1,400&display=swap">
<style>
:root{
  --board:#5b5b5b;
  --paper:#ffffff;
  --panel:#a3a5a8;
  --teal:#86d0d6;
  --teal-deep:#5fbcc4;
  --ink:#6d6e70;
  --ink-soft:#8a8b8d;
  --skin:#e9cfc0;
  --skin-deep:#c99a80;
  --rose:#efe3de;
  --white-line:rgba(255,255,255,.85);
}
*{box-sizing:border-box;margin:0;padding:0}
html,body{width:1200px;height:3399px;overflow:hidden;background:var(--board)}
body{position:relative;font-family:"Open Sans",Arial,sans-serif;color:var(--ink)}
.page{position:absolute;width:461px;height:338px;background:var(--paper);overflow:hidden}
.col-l{left:125px}.col-r{left:625px}
.r0{top:80px}.r1{top:440px}.r2{top:799px}.r3{top:1159px}.r4{top:1518px}
.r5{top:1877px}.r6{top:2237px}.r7{top:2596px}.r8{top:2955px}

/* wordmark */
.wordmark{font-weight:300;letter-spacing:.32em;text-transform:uppercase;color:var(--ink);display:flex;align-items:center;gap:8px}
.wordmark .dot{width:6px;height:6px;background:var(--teal)}
.wordmark-sub{font-size:5px;letter-spacing:.35em;text-transform:uppercase;color:var(--ink-soft);margin-top:5px}

/* cover */
.cover .brand{position:absolute;left:0;right:0;top:150px;display:flex;flex-direction:column;align-items:center}
.cover .wordmark{font-size:15px}
.cover .web{position:absolute;right:14px;bottom:13px;display:flex;align-items:center;gap:6px;font-size:6px;color:var(--ink-soft)}
.cover .web i{display:block;width:26px;height:5px;background:var(--teal)}

/* panels */
.panel{position:absolute;inset:14px;background:var(--panel)}
.frame{position:absolute;border:1px solid var(--white-line);color:#fff;font-size:6.4px;line-height:1.55}
.frame.italic{font-style:italic;font-weight:300}
.frame p+p{margin-top:6px}
.panel-note{position:absolute;left:0;right:0;text-align:center;color:#fff;font-size:8px;line-height:1.6}

/* photos */
.photo{position:absolute}
.ph-face{background:radial-gradient(ellipse at 45% 45%,#f3dccd 0%,#e2bda6 45%,#cfa38a 100%)}
.ph-skin{background:linear-gradient(135deg,#f2e2d8 0%,#e4c2ad 55%,#c99a80 100%)}
.ph-wax{background:linear-gradient(120deg,#f4e3d6 0%,#d9a777 50%,#b97c4c 100%)}
.ph-lash{background:linear-gradient(160deg,#f6eeea 0%,#e7cbbd 55%,#c9a594 100%)}
.ph-tan{background:linear-gradient(150deg,#f1ede9 0%,#d4a17c 50%,#a36a46 100%)}
.ph-cream{background:linear-gradient(180deg,#f2d7b4 0%,#d8a25f 45%,#f2f2ef 100%)}

.tag{position:absolute;background:var(--teal);color:#fff;font-weight:300;line-height:1.25;padding:8px 10px}

/* copy */
.copy{position:absolute;font-size:5.6px;line-height:1.55;color:var(--ink)}
.copy h2{color:var(--teal-deep);font-weight:400;font-size:9px;margin:0 0 5px}
.copy h2+p,.copy p+p{margin-top:0}
.copy p{margin-bottom:5px}
.copy ul{list-style:none;margin:0 0 5px}
.copy li{padding-left:7px;position:relative}
.copy li::before{content:"";position:absolute;left:0;top:2.5px;width:3px;height:3px;border-radius:50%;background:var(--ink-soft)}
.price{color:var(--teal-deep);text-align:right;display:block}
.callout{background:var(--teal);color:#fff;padding:6px 7px;margin-top:6px}
.callout strong{display:block;font-weight:600;font-size:6.4px;margin-bottom:3px}
.rates{width:100%;border-collapse:collapse;font-size:5.6px}
.rates td{padding:1.6px 0;border-bottom:1px solid #e4e4e4}
.rates td:last-child{text-align:right;color:var(--ink)}
.partner{position:absolute;font-size:12px;font-weight:600;letter-spacing:.2em;color:var(--ink)}

/* back */
.back{background:var(--teal)}
.back-card{position:absolute;left:70px;top:105px;width:318px;height:100px;background:#fff;display:flex;align-items:center;padding:0 28px;gap:30px}
.back-card .wordmark{font-size:10px;flex-direction:column;gap:4px}
.back-card address{font-style:normal;font-size:5.4px;line-height:1.6;color:var(--ink-soft)}
</style>
</head>
<body>

<!-- row 0 -->
<section class="page col-r r0 cover">
  <div class="brand">
    <div class="wordmark"><span class="dot"></span>Atelier Kova</div>
    <div class="wordmark-sub">Schoonheidsinstituut</div>
  </div>
  <div class="web">www.atelierkova.be <i></i></div>
</section>

<!-- row 1 -->
<section class="page col-l r1">
  <div class="panel">
    <div class="frame italic" style="left:58px;top:70px;width:318px;height:170px;padding:20px 22px">
      <p>Al meer dan 5 jaar ben ik met veel passie en enthousiasme klaar om mijn klanten met de glimlach te ontvangen. Mijn specialiteiten zijn gelaatsverzorgingen met de kwalitatieve producten van Lunelle, wimperextensions, suikerontharing en Permanente Make Up.</p>
      <p>Ik volg regelmatig bijscholingen om bij te blijven met de nieuwste trends.</p>
      <p>Lotte Verhaegen, uw schoonheidsspecialiste</p>
    </div>
  </div>
</section>
<section class="page col-r r1">
  <div class="photo ph-face" role="img" aria-label="Portret van de schoonheidsspecialiste" style="left:14px;top:14px;width:300px;bottom:14px"></div>
  <div class="wordmark" style="position:absolute;right:18px;top:26px;font-size:5px">Atelier Kova</div>
  <div class="tag" style="right:26px;top:168px;width:78px;font-size:14px">Steeds tot uw dienst</div>
</section>

<!-- row 2 -->
<section class="page col-l r2">
  <div class="photo ph-skin" role="img" aria-label="Behandeling permanente make-up van de wenkbrauwen" style="left:8px;top:8px;width:205px;bottom:8px"></div>
  <div class="copy" style="left:228px;top:22px;width:205px">
    <h2>Permanente Make Up</h2>
    <p>Permanente make-up zet uw natuurlijke schoonheid subtiel in de verf. Wenkbrauwen, eyeliner of lippen krijgen een blijvende en verzorgde uitstraling die dagelijks tijd bespaart en perfect past bij uw gelaat.</p>
    <p>Met fijne pigmenten en een zachte techniek werken we laag per laag tot het gewenste resultaat. Het effect blijft enkele jaren zichtbaar en vervaagt geleidelijk.</p>
    <p>Een bijwerking na zes tot acht weken is inbegrepen, zodat kleur en vorm mooi egaal blijven en u volledig tevreden bent.</p>
    <div class="callout"><strong>GRATIS ADVIESGESPREK</strong>Voor elke behandeling nemen we rustig de tijd om samen met u de vorm en kleur te bepalen die het best bij u passen.</div>
  </div>
</section>
<section class="page col-r r2">
  <div class="copy" style="left:22px;top:22px;width:200px">
    <h2>Waarom u Permanente Make Up Zou?</h2>
    <ul>
      <li>U heeft elke dag een verzorgde look, ook na het sporten</li>
      <li>U bespaart tijd bij het opmaken in de ochtend</li>
      <li>Ideaal bij dunne of onregelmatige wenkbrauwen</li>
      <li>Geschikt voor wie allergisch is voor gewone make-up</li>
      <li>Uw ogen en lippen komen mooi tot hun recht</li>
      <li>Het resultaat oogt natuurlijk en subtiel</li>
    </ul>
    <h2 style="margin-top:8px">TARIEVEN</h2>
    <table class="rates">
      <tr><td>Fijne eyeliner bovenrand</td><td>€180</td></tr>
      <tr><td>Brede eyeliner bovenrand</td><td>€220</td></tr>
      <tr><td>Eyeliner onderrand</td><td>€150</td></tr>
      <tr><td>Wenkbrauwen haartjestechniek</td><td>€350</td></tr>
      <tr><td>Wenkbrauwen poedereffect</td><td>€350</td></tr>
      <tr><td>Full lips</td><td>€400</td></tr>
    </table>
  </div>
  <div class="photo ph-face" role="img" aria-label="Close-up van een gelaat met verzorgde wenkbrauwen" style="right:8px;top:8px;width:210px;bottom:8px"></div>
</section>

<!-- row 3 -->
<section class="page col-l r3">
  <div class="photo ph-face" role="img" aria-label="Vrouw met stralende huid na gelaatsverzorging" style="left:8px;top:8px;width:205px;bottom:60px"></div>
  <div class="partner" style="left:70px;top:294px">LUNELLE</div>
  <div class="copy" style="left:228px;top:22px;width:205px">
    <h2>Gelaatsverzorging Lunelle</h2>
    <p>Elke verzorging begint met een grondige analyse van uw huid, zodat we de juiste producten kiezen voor een zichtbaar en blijvend resultaat.</p>
    <ul><li>Een zachte reiniging van het gelaat</li><li>Een peeling op maat van uw huid</li><li>Een ontspannende massage</li></ul>
    <h2>Cosmetische Verzorging</h2>
    <p>Reiniging, peeling, epilatie van de wenkbrauwen, masker en aangepaste dagverzorging.</p>
    <span class="price">€58</span>
    <h2>Verzorging voor gevoelige huid</h2>
    <p>Een kalmerende behandeling die roodheid vermindert.</p>
    <span class="price">€62</span>
    <h2>Flash Nettoyant</h2>
    <p>Een snelle reiniging die uw huid onmiddellijk fris en helder maakt.</p>
    <span class="price">€38 · 30 min</span>
  </div>
</section>
<section class="page col-r r3">
  <div class="copy" style="left:22px;top:22px;width:200px">
    <h2>Hydratation Essentielle</h2>
    <p>Een intens hydraterende verzorging voor de droge huid. Reiniging, peeling, massage en een voedend masker geven uw huid haar soepelheid terug.</p>
    <span class="price">€65 · 60 min</span>
    <h2>Pureté Essentielle</h2>
    <p>Speciaal ontwikkeld voor de gemengde tot vette huid. De poriën worden gezuiverd en de huid krijgt een matte, frisse uitstraling.</p>
    <span class="price">€65 · 60 min</span>
    <h2>Luxe Verzorging Supreme Experience</h2>
    <p>Onze meest verfijnde behandeling met een uitgebreide massage, serum en masker op maat voor een zichtbaar verjongd gelaat.</p>
    <span class="price">€85 · 90 min</span>
  </div>
  <div class="photo ph-face" role="img" aria-label="Vrouw die haar wang aanraakt" style="right:8px;top:8px;width:210px;bottom:8px"></div>
</section>

<!-- row 4 -->
<section class="page col-l r4">
  <div class="photo ph-wax" role="img" aria-label="Suikerpasta wordt op een been aangebracht" style="left:8px;top:8px;width:205px;bottom:8px"></div>
  <div class="copy" style="left:228px;top:22px;width:205px">
    <h2>Ontharing Met Suiker</h2>
    <p>Suikerontharing is een natuurlijke en zachte methode die al eeuwen wordt toegepast. De pasta bestaat uit suiker, citroen en water.</p>
    <ul>
      <li>De haartjes worden in de groeirichting verwijderd</li>
      <li>Minder pijnlijk dan traditionele wax</li>
      <li>Geschikt voor de gevoelige huid</li>
      <li>Geen risico op verbranding</li>
      <li>Minder ingegroeide haartjes</li>
      <li>Het resultaat blijft tot vier weken mooi</li>
      <li>De haargroei wordt na verloop van tijd fijner</li>
      <li>Volledig natuurlijke ingrediënten</li>
      <li>Zeer hygiënisch: de pasta wordt per klant gebruikt</li>
    </ul>
  </div>
</section>
<section class="page col-r r4">
  <div class="copy" style="left:22px;top:22px;width:200px">
    <h2>TARIEVEN</h2>
    <table class="rates">
      <tr><td>Wenkbrauwen</td><td>€9</td></tr>
      <tr><td>Wenkbrauwen en bovenlip</td><td>€14</td></tr>
      <tr><td>Bovenlip of kin</td><td>€6</td></tr>
      <tr><td>Bovenlip en kin</td><td>€10</td></tr>
      <tr><td>Gezicht volledig</td><td>€22</td></tr>
      <tr><td>Oksels</td><td>€12</td></tr>
      <tr><td>Armen</td><td>€20</td></tr>
      <tr><td>Bikinilijn</td><td>€14</td></tr>
      <tr><td>Brazilian</td><td>€32</td></tr>
      <tr><td>Onderbenen en knie</td><td>€24</td></tr>
      <tr><td>Bovenbenen</td><td>€22</td></tr>
      <tr><td>Volledige benen</td><td>€38</td></tr>
      <tr><td>Volledige benen en bikinilijn</td><td>€48</td></tr>
    </table>
  </div>
  <div class="photo ph-cream" role="img" aria-label="Pot met suikerpasta en spatel" style="right:8px;top:8px;width:210px;bottom:8px"></div>
  <div class="wordmark" style="position:absolute;left:96px;top:290px;font-size:5px">Atelier Kova</div>
</section>

<!-- row 5 -->
<section class="page col-l r5">
  <div class="panel">
    <div class="frame" style="left:28px;top:40px;width:180px;height:170px;padding:14px 12px">
      <p>Lange, volle en gekrulde wimpers zonder mascara? Bij wimperverlenging wordt elke extension afzonderlijk op een natuurlijke wimper geplaatst. Het resultaat is een open blik die er natuurlijk uitziet.</p>
      <p>Met een goede verzorging blijft het effect weken mooi. Na maximaal vier weken plannen we een bijwerking om uitgevallen wimpers te vervangen.</p>
    </div>
    <div class="frame" style="left:220px;top:40px;width:190px;height:170px;padding:14px 12px">
      <p>Voordelen van Lash Atelier wimperverlenging:</p>
      <p>· Perfect afgewerkt ·  Geen mascara meer nodig · Volledig op maat · Waterbestendig · Licht en comfortabel · Lang houdbaar · Natuurlijke uitstraling · Ook bij korte wimpers · Elke dag klaar</p>
    </div>
    <div class="panel-note" style="top:224px">Eerste plaatsing wimperextensions €65<br>Bijwerking na max. 4 weken €35</div>
  </div>
</section>
<section class="page col-r r5">
  <div class="photo ph-lash" role="img" aria-label="Plaatsing van wimperextensions met pincet" style="left:14px;top:14px;right:14px;bottom:14px"></div>
  <div class="tag" style="left:32px;top:224px;width:108px;font-size:9.5px">Individuele Wimperverlenging Lash Atelier</div>
</section>

<!-- row 6 -->
<section class="page col-l r6">
  <div class="photo ph-lash" role="img" aria-label="Oog voor wimperlifting" style="left:14px;top:14px;width:210px;height:150px"></div>
  <div class="photo ph-lash" role="img" aria-label="Oog na wimperlifting" style="left:236px;top:14px;width:211px;height:150px"></div>
  <div class="photo ph-skin" role="img" aria-label="Close-up van opgekrulde wimpers" style="left:14px;top:174px;width:433px;height:150px"></div>
  <div class="tag" style="left:178px;top:140px;width:105px;font-size:9.5px;text-align:center">Wimperlifting Lift Lashes</div>
</section>
<section class="page col-r r6">
  <div class="panel">
    <div class="frame italic" style="left:70px;top:52px;width:295px;height:150px;padding:16px 18px">
      <p>Het heffen van mooie, lange en volumineuze wimpers vloeit hoog op het verlanglijstje van vele vrouwen. Het liefst hoeft men de wimpers zo weinig mogelijk te krullen met een tang, zodat ze gezond blijven.</p>
      <p>De nieuwe en revolutionaire liftmethode zorgt ervoor dat na één behandeling van 60 minuten uw wimpers tot acht weken mooi gekruld en langer lijken, zonder mascara of extensions.</p>
    </div>
    <div class="panel-note" style="top:222px">Wimperlifting €65</div>
  </div>
</section>

<!-- row 7 -->
<section class="page col-l r7">
  <div class="photo ph-tan" role="img" aria-label="Gebruinde huid na airbrush tanning" style="left:8px;top:8px;width:205px;bottom:8px"></div>
  <div class="copy" style="left:228px;top:22px;width:205px">
    <h2>Airbrush Tanning</h2>
    <p>Wilt u snel een gezonde, natuurlijke bruine teint zonder schadelijke zonnestralen? Met airbrush tanning krijgt u in enkele minuten een egale kleur die perfect aansluit bij uw huidtype.</p>
    <p>De spray bevat verzorgende ingrediënten die de huid hydrateren en een streepvrij resultaat geven.</p>
    <h2>De Airbrush Tanning Zelf</h2>
    <p>Na een korte voorbereiding wordt de lotion in een fijne nevel over het lichaam aangebracht. De kleur ontwikkelt zich binnen enkele uren en blijft tot een week mooi zichtbaar.</p>
  </div>
  <div class="copy" style="left:228px;bottom:18px;width:205px;font-size:6.4px">Volledige tanning van het volledige lichaam <span style="color:var(--teal-deep);float:right">€35</span></div>
</section>
<section class="page col-r r7">
  <div class="panel">
    <div class="frame" style="left:60px;top:50px;width:313px;height:205px;padding:22px 20px">
      <p>Atelier Kova Schoonheidsinstituut is gevestigd op een rustige ligging met vlotte bereikbaarheid en ruime parking. U bent van harte welkom voor een verzorging op maat in een stijlvolle omgeving.</p>
      <p>Voordelen van Atelier Kova:</p>
      <p>· Je kan snel online een afspraak maken<br>· Kwaliteitsvolle producten voor elk huidtype<br>· Parking aan de deur voor uw gemak<br>· Deskundig advies door een ervaren specialiste<br>· Cadeaubonnen voor elke gelegenheid<br>· Discreet en persoonlijk onthaal</p>
    </div>
  </div>
</section>

<!-- row 8 -->
<section class="page col-l r8 back">
  <div class="back-card">
    <div class="wordmark"><span class="dot"></span>Atelier Kova</div>
    <address>Atelier Kova Schoonheidsinstituut<br>Lindenlaan 12, 9000 Gent<br>0479 58 21 64<br>info@atelierkova.be<br>www.atelierkova.be</address>
  </div>
</section>

</body>
</html>
```